Bref créative
Larchmere Restoring LLC
Bringing new life to old wood
Professional
Trent Holloway
owner
larchmererestore@mailvox.net
I need the following listed on the card.
Owners:
Trent Holloway 555 274 1906
Darby Fennimore 555 381 4527
Licensed and Insured
Free Estimates.
Hardwood floors and Cabinets. If it's made of wood we can renew it. Color changes or tints. Low odor, dust, and mess. A fraction of the cost vs refacing or replacement. Quick turnaround. Most jobs completed in 1-2 days.

```html
<!DOCTYPE html>
<html lang="en">
<head>
<meta charset="utf-8">
<title>Larchmere Restoring LLC — Stationery Set</title>
<link href="https://fonts.googleapis.com/css2?family=Raleway:wght@300;400;600&display=swap" rel="stylesheet">
<style>
  :root {
    --backdrop: #d9d9d9;
    --paper: #ffffff;
    --wood-light: #e6cfa3;
    --wood-mid: #d6b783;
    --wood-dark: #c29d63;
    --ink: #5b5b5b;
    --ink-soft: #8f8f8f;
    --rule: #bdbdbd;
    --ghost: #ececec;
    --mark: #6f6255;
  }
  * { box-sizing: border-box; margin: 0; padding: 0; }
  html, body { width: 1200px; height: 468px; overflow: hidden; }
  body {
    background: var(--backdrop);
    font-family: "Raleway", sans-serif;
    color: var(--ink);
    position: relative;
  }
  .sheet, .envelope, .card {
    position: absolute;
    background: var(--paper);
    box-shadow: 0 2px 6px rgba(0,0,0,.18);
    overflow: hidden;
  }
  .wood {
    position: absolute;
    background: linear-gradient(90deg, var(--wood-mid), var(--wood-light) 45%, var(--wood-dark));
  }
  .brand-mark {
    position: absolute;
    width: 22px; height: 22px;
    background: var(--mark);
  }
  .brand-name {
    position: absolute;
    font-weight: 600;
    color: var(--ink);
    letter-spacing: .04em;
    text-transform: uppercase;
    line-height: 1.15;
  }
  .contact {
    position: absolute;
    font-size: 4.6px;
    line-height: 1.5;
    color: var(--ink-soft);
  }
  .ghost-name {
    position: absolute;
    font-weight: 300;
    color: var(--ghost);
    text-transform: uppercase;
    letter-spacing: .1em;
    text-align: center;
    line-height: 1.1;
  }
  .footer-note {
    position: absolute;
    font-size: 4px;
    color: var(--ink-soft);
  }

  /* Letterhead */
  .letterhead { left: 34px; top: 48px; width: 230px; height: 336px; }
  .letterhead .wood { left: 0; top: 0; width: 30px; height: 100%; }
  .letterhead .brand-mark { left: 4px; top: 8px; }
  .letterhead .brand-name { left: 36px; top: 10px; font-size: 5.5px; }
  .letterhead .contact.left { left: 36px; top: 24px; }
  .letterhead .contact.right { left: 150px; top: 10px; }
  .letterhead .ghost-name { left: 40px; top: 140px; width: 180px; font-size: 16px; }
  .letterhead .footer-note { left: 36px; bottom: 10px; }

  /* Fax */
  .fax { left: 307px; top: 48px; width: 240px; height: 336px; }
  .fax .wood { left: 0; top: 0; width: 30px; height: 100%; }
  .fax .brand-mark { left: 4px; top: 8px; }
  .fax .brand-name { left: 36px; top: 10px; font-size: 5.5px; }
  .fax .contact.right { left: 160px; top: 10px; }
  .fax-title { position: absolute; left: 38px; top: 42px; font-size: 15px; font-weight: 400; letter-spacing: .05em; }
  .fax-fields { position: absolute; left: 38px; top: 66px; width: 190px; }
  .fax-fields svg { display: block; }
  .fax .footer-note { left: 36px; bottom: 10px; }

  /* Envelopes */
  .envelope.back { left: 691px; top: 24px; width: 490px; height: 156px; background: #f4f4f4; }
  .envelope.back .brand-mark { left: 234px; top: 16px; }
  .envelope.front { left: 677px; top: 115px; width: 482px; height: 197px; }
  .envelope.front .wood { left: 0; top: 0; width: 32px; height: 100%; }
  .envelope.front .brand-mark { left: 5px; top: 8px; }
  .envelope.front .brand-name { left: 40px; top: 12px; font-size: 6px; }
  .envelope.front .contact { left: 40px; top: 26px; }

  /* Cards */
  .card { top: 329px; height: 43px; }
  .card.front { left: 763px; width: 89px; }
  .card.front .wood { left: 0; top: 0; width: 11px; height: 100%; }
  .card.front .brand-mark { left: 14px; top: 4px; width: 9px; height: 9px; }
  .card.front .brand-name { left: 14px; top: 15px; font-size: 3.6px; }
  .card.front .contact { left: 14px; top: 24px; font-size: 2.6px; line-height: 1.35; }
  .card.back { left: 864px; width: 96px; background: var(--wood-light); }
  .card.back .tagline { position: absolute; left: 6px; top: 5px; font-size: 3.6px; font-weight: 600; color: var(--ink); }
  .card.back .services { position: absolute; left: 6px; top: 11px; width: 86px; font-size: 2.5px; line-height: 1.4; color: var(--ink); }
</style>
</head>
<body>

  <!-- Letterhead -->
  <section class="sheet letterhead">
    <div class="wood" role="img" aria-label="Light oak wood grain strip"></div>
    <div class="brand-mark"></div>
    <div class="brand-name">Larchmere<br>Restoring LLC</div>
    <div class="contact left">Bringing new life to old wood<br>Licensed and Insured</div>
    <div class="contact right">Trent Holloway 555 274 1906<br>Darby Fennimore 555 381 4527<br>larchmererestore@mailvox.net</div>
    <div class="ghost-name">Larchmere<br>Restoring</div>
    <div class="footer-note">Licensed and Insured · Free Estimates</div>
  </section>

  <!-- Fax cover -->
  <section class="sheet fax">
    <div class="wood" role="img" aria-label="Light oak wood grain strip"></div>
    <div class="brand-mark"></div>
    <div class="brand-name">Larchmere<br>Restoring LLC</div>
    <div class="contact right">555 274 1906<br>555 381 4527<br>larchmererestore@mailvox.net</div>
    <div class="fax-title">FAX</div>
    <div class="fax-fields">
      <svg width="190" height="100" viewBox="0 0 190 100" font-family="Raleway, sans-serif" font-size="4.5" fill="#8f8f8f">
        <g stroke="#bdbdbd" stroke-width=".6">
          <line x1="12" y1="10" x2="90" y2="10"/><line x1="112" y1="10" x2="190" y2="10"/>
          <line x1="12" y1="22" x2="90" y2="22"/><line x1="112" y1="22" x2="190" y2="22"/>
          <line x1="12" y1="34" x2="90" y2="34"/><line x1="112" y1="34" x2="190" y2="34"/>
          <line x1="12" y1="46" x2="90" y2="46"/><line x1="112" y1="46" x2="190" y2="46"/>
          <line x1="0" y1="58" x2="190" y2="58"/>
        </g>
        <text x="0" y="9">To:</text><text x="96" y="9">From:</text>
        <text x="0" y="21">Fax:</text><text x="96" y="21">Pages:</text>
        <text x="0" y="33">Phone:</text><text x="96" y="33">Date:</text>
        <text x="0" y="45">Re:</text><text x="96" y="45">CC:</text>
        <g fill="none" stroke="#8f8f8f" stroke-width=".6">
          <rect x="0" y="66" width="4" height="4"/><rect x="38" y="66" width="4" height="4"/>
          <rect x="80" y="66" width="4" height="4"/><rect x="122" y="66" width="4" height="4"/>
          <rect x="158" y="66" width="4" height="4"/>
        </g>
        <text x="6" y="69.5">Urgent</text><text x="44" y="69.5">For Review</text>
        <text x="86" y="69.5">Please Comment</text><text x="128" y="69.5">Please Reply</text>
        <text x="164" y="69.5">Recycle</text>
      </svg>
    </div>
    <div class="footer-note">Licensed and Insured · Free Estimates</div>
  </section>

  <!-- Envelope, back flap -->
  <section class="envelope back">
    <svg width="490" height="156" viewBox="0 0 490 156" style="position:absolute;left:0;top:0">
      <polyline points="0,0 245,70 490,0" fill="none" stroke="#cfcfcf" stroke-width="1"/>
    </svg>
    <div class="brand-mark"></div>
  </section>

  <!-- Envelope, front -->
  <section class="envelope front">
    <div class="wood" role="img" aria-label="Light oak wood grain strip"></div>
    <div class="brand-mark"></div>
    <div class="brand-name">Larchmere Restoring LLC</div>
    <div class="contact">larchmererestore@mailvox.net<br>555 274 1906</div>
  </section>

  <!-- Business card, front -->
  <section class="card front">
    <div class="wood" role="img" aria-label="Light oak wood grain strip"></div>
    <div class="brand-mark"></div>
    <div class="brand-name">Larchmere Restoring LLC</div>
    <div class="contact">Trent Holloway, owner · 555 274 1906<br>Darby Fennimore · 555 381 4527<br>larchmererestore@mailvox.net</div>
  </section>

  <!-- Business card, back -->
  <section class="card back">
    <div class="tagline">Bringing new life to old wood</div>
    <div class="services">Hardwood floors and Cabinets. If it's made of wood we can renew it. Color changes or tints. Low odor, dust, and mess. A fraction of the cost vs refacing or replacement. Most jobs done in 1-2 days. Licensed and Insured. Free Estimates.</div>
  </section>

</body>
</html>
```